European Indian Investment firm

I would like to have a complete make-over of an existing website. Have a look at : www.velmoranpartners-example.com
We are a European/Indian based investment firm that acquires stakes in European (Manufacturing) companies (industrial) and help them grow in India. We have a team in Europe (Barcelona, Zurich, Amsterdam) and in India (Bangalore).
Amongst the new lay-out of the website also the name and the logo of the site will change. I will upload the new company logo. The new site should broadly send out the same message which is bridging Europe and India and also it should have an industrial/manufacturing look. The wording and the various pages of the website will be broadly the same as the old one with some changes which we will provide further down the road. I

Target Market(s)

Europe and India. Entrepreneurs, CEO's and investors.

Industry/Entity Type

Investment

Coding

Coded - Design and coding required

Number of Pages Required

5+ page

Font styles to use
Sans Serif

Requirements
Must have
• site should have an industrial look and also it should reflect the bridging between the two continents Europe and India provided by the team helping companies to grow.

```html
<!DOCTYPE html>
<html lang="en">
<head>
<meta charset="utf-8">
<title>Velmoran Capital Partners</title>
<link href="https://fonts.googleapis.com/css2?family=Oswald:wght@400;500&family=Open+Sans:wght@400;600&display=swap" rel="stylesheet">
<style>
:root{
  --teal:#1f5a68;
  --teal-dark:#174652;
  --tan:#cbb68f;
  --gold:#d7a244;
  --ink:#333;
  --muted:#8a8a8a;
  --line:#e3e3e3;
  --footer:#262626;
  --white:#fff;
}
*{margin:0;padding:0;box-sizing:border-box}
html,body{width:887px;height:1200px;overflow:hidden;background:var(--white)}
body{font-family:"Open Sans",Arial,sans-serif;color:var(--ink);position:relative}
.header{height:95px;display:flex;align-items:center;justify-content:space-between;padding:0 68px 0 80px}
.brand{display:flex;align-items:center;gap:10px}
.brand-mark{width:22px;height:22px;background:var(--teal)}
.brand-name{font-family:"Oswald",sans-serif;font-weight:500;font-size:17px;color:var(--teal);letter-spacing:1px;line-height:1.05;text-transform:uppercase}
.nav{display:flex;gap:4px}
.nav a{font-family:"Oswald",sans-serif;font-size:11px;color:var(--ink);text-decoration:none;padding:14px 13px;letter-spacing:.5px}
.nav a.active{background:var(--teal);color:var(--white)}
.hero{position:relative;height:415px;background:linear-gradient(100deg,#cfd3d6 0%,#e9ecee 35%,#b7bec3 60%,#8f979c 100%)}
.hero-overlay{position:absolute;inset:0;display:flex;flex-direction:column;align-items:center;justify-content:center;text-align:center;padding-bottom:40px}
.hero h1{font-family:"Oswald",sans-serif;font-weight:500;font-size:27px;color:var(--white);letter-spacing:.5px;text-shadow:0 1px 3px rgba(0,0,0,.35)}
.hero p{width:440px;margin-top:10px;font-size:10px;line-height:1.6;color:var(--white);text-shadow:0 1px 2px rgba(0,0,0,.4)}
.hero-dots{display:flex;gap:8px;margin-top:16px}
.hero-dots span{width:10px;height:10px;border-radius:50%;background:rgba(255,255,255,.6)}
.hero-dots span.on{background:var(--white)}
.features{display:flex;gap:20px;padding:0 70px;margin-top:40px}
.feature{width:170px;height:165px;background:var(--teal);color:var(--white);text-align:center;position:relative}
.feature-icon{width:38px;height:38px;border-radius:50%;border:2px solid var(--white);margin:16px auto 8px;display:flex;align-items:center;justify-content:center;font-family:"Oswald",sans-serif;font-size:18px}
.feature h3{font-family:"Oswald",sans-serif;font-weight:400;font-size:13px;letter-spacing:.5px}
.feature p{font-size:9px;line-height:1.5;padding:6px 18px 0;color:#d8e3e6}
.feature .more{position:absolute;left:0;right:0;bottom:0;height:24px;background:var(--tan);color:var(--teal-dark);font-size:8px;font-weight:600;line-height:24px;letter-spacing:.5px}
.main{display:flex;padding:0 68px 0 70px;margin-top:40px;gap:48px}
.welcome{width:530px}
.section-title{font-family:"Oswald",sans-serif;font-weight:500;font-size:21px;color:var(--teal);text-transform:uppercase;padding-bottom:8px;border-bottom:1px solid var(--line)}
.section-title em{font-style:normal;color:var(--gold)}
.welcome-row{display:flex;gap:16px;margin-top:16px}
.welcome-photo{width:180px;height:130px;flex:none;background:linear-gradient(135deg,#dfe7ee,#a9b8c2)}
.welcome p{font-size:10px;line-height:1.7;color:var(--muted)}
.welcome .body{margin-top:12px}
.read{display:inline-block;margin-top:12px;font-size:9px;font-weight:600;color:var(--ink);letter-spacing:.5px}
.read::after{content:"";display:inline-block;width:9px;height:9px;border-radius:50%;background:var(--ink);margin-left:6px;vertical-align:-1px}
.news{width:171px}
.news-item{display:flex;gap:9px;margin-top:14px}
.news-thumb{width:40px;height:40px;flex:none;background:linear-gradient(135deg,#c9d3d9,#8e9ca5)}
.news-date{font-size:8px;color:var(--teal);font-weight:600}
.news-text{font-size:8.5px;line-height:1.45;color:var(--muted)}
.footer{position:absolute;left:0;right:0;bottom:0;height:140px;background:var(--footer);color:var(--white);text-align:center}
.social{display:flex;justify-content:center;gap:8px;padding-top:28px}
.social span{width:22px;height:22px;border-radius:50%;background:var(--white)}
.footer-nav{margin-top:26px;font-size:8.5px;letter-spacing:.5px}
.footer-nav span{margin:0 6px}
.copy{margin-top:8px;font-size:7.5px;color:#9a9a9a}
</style>
</head>
<body>
<header class="header">
  <div class="brand"><span class="brand-mark"></span><span class="brand-name">Velmoran<br>Capital Partners</span></div>
  <nav class="nav">
    <a class="active">HOME</a><a>STRATEGY</a><a>TEAM</a><a>PORTFOLIO</a><a>PUBLICATIONS</a><a>INVESTORS</a><a>CONTACT</a>
  </nav>
</header>

<section class="hero">
  <div role="img" aria-label="Photo of a business handshake in a bright office" style="position:absolute;inset:0"></div>
  <div class="hero-overlay">
    <h1>A EURO/INDIAN INVESTMENT PLATFORM</h1>
    <p>We acquire stakes in European industrial companies and help them grow across India, bridging two continents with one dedicated team.</p>
    <div class="hero-dots"><span class="on"></span><span></span><span></span></div>
  </div>
</section>

<section class="features">
  <div class="feature">
    <div class="feature-icon">
      <svg width="18" height="18" viewBox="0 0 18 18" fill="#fff"><circle cx="9" cy="5" r="3.5"/><path d="M2 17c0-4 3-6.5 7-6.5s7 2.5 7 6.5z"/></svg>
    </div>
    <h3>ABOUT US</h3>
    <p>A European and Indian team building lasting industrial partnerships.</p>
    <div class="more">READ MORE ›</div>
  </div>
  <div class="feature">
    <div class="feature-icon">
      <svg width="18" height="18" viewBox="0 0 18 18" fill="#fff"><rect x="2" y="10" width="3" height="6"/><rect x="7.5" y="6" width="3" height="10"/><rect x="13" y="2" width="3" height="14"/></svg>
    </div>
    <h3>STRATEGY</h3>
    <p>Stakes in mid-sized manufacturers with strong growth potential in India.</p>
    <div class="more">READ MORE ›</div>
  </div>
  <div class="feature">
    <div class="feature-icon">
      <svg width="18" height="18" viewBox="0 0 18 18" fill="#fff"><rect x="1" y="5" width="16" height="11" rx="1"/><rect x="6" y="2" width="6" height="4" fill="none" stroke="#fff" stroke-width="1.5"/></svg>
    </div>
    <h3>PORTFOLIO</h3>
    <p>Industrial companies we support on their path into Asia.</p>
    <div class="more">READ MORE ›</div>
  </div>
  <div class="feature">
    <div class="feature-icon">€</div>
    <h3>INVESTORS</h3>
    <p>Partnering with entrepreneurs and investors who share our vision.</p>
    <div class="more">READ MORE ›</div>
  </div>
</section>

<section class="main">
  <div class="welcome">
    <h2 class="section-title">Welcome to <em>Velmoran Capital Partners</em></h2>
    <div class="welcome-row">
      <div class="welcome-photo" role="img" aria-label="Photo of a team meeting in a modern office"></div>
      <p>Our team in Barcelona, Zurich, Amsterdam and Bangalore works side by side with owners and managers to open new markets, set up local operations and build strong supply chains for European manufacturers.</p>
    </div>
    <p class="body">We bring capital, industrial know-how and a local network in India. Each partnership is long term and hands-on, focused on sustainable growth, operational excellence and shared value for all stakeholders.</p>
    <span class="read">READ MORE</span>
  </div>
  <aside class="news">
    <h2 class="section-title">Latest <em>News</em></h2>
    <div class="news-item">
      <div class="news-thumb" role="img" aria-label="News photo"></div>
      <div><div class="news-date">12.05.2015</div><div class="news-text">New partnership signed with a Dutch machinery maker.</div></div>
    </div>
    <div class="news-item">
      <div class="news-thumb" role="img" aria-label="News photo"></div>
      <div><div class="news-date">28.04.2015</div><div class="news-text">Bangalore office expands its engineering advisory team.</div></div>
    </div>
    <div class="news-item">
      <div class="news-thumb" role="img" aria-label="News photo"></div>
      <div><div class="news-date">09.04.2015</div><div class="news-text">Zurich investor meeting on Indo-European growth.</div></div>
    </div>
    <span class="read">READ MORE</span>
  </aside>
</section>

<footer class="footer">
  <div class="social"><span></span><span></span><span></span><span></span><span></span><span></span><span></span><span></span></div>
  <div class="footer-nav"><span>HOME</span>/<span>ABOUT US</span>/<span>STRATEGY</span>/<span>TEAM</span>/<span>PORTFOLIO</span>/<span>INVESTORS</span>/<span>CONTACT US</span></div>
  <div class="copy">© 2015 Velmoran Capital Partners. All Rights Reserved.</div>
</footer>
</body>
</html>
```